Night Dresses business cards business requirers

We are a new company initiating Mexico operations. Our core business is Night woman dress (both formal and party dress) for rent. Gownhaven is the name of the company. ITS Gownhaven form by two word. The dress word and topia (Utopic) so the place Gownhaven Means That You cant get the ideal, perfect and unique dress for your event. So we would like a modern, very creative, and attractive business card.

Industry/Entity Type

Womens Clothing

Contact Information for Business Card

Rounded Borders, two faces

Requirements
Must have
• Rounded borders, logo and slogan, modern, glam, attractive design
Should not have
• modern design classic or not

```html
<!DOCTYPE html>
<html lang="en">
<head>
<meta charset="UTF-8">
<title>Gownhaven — Business Card, Two Faces</title>
<link href="https://fonts.googleapis.com/css2?family=Open+Sans:wght@400;600&display=swap" rel="stylesheet">
<style>
  :root {
    --backdrop: #e6d6d7;
    --card-white: #ffffff;
    --plum: #a2477f;
    --plum-line: #b0508c;
    --magenta: #b9609b;
    --magenta-soft: #d58cc0;
    --blush: #f0c6d3;
    --panel: rgba(110, 40, 85, 0.62);
    --ink-grey: #4a4a4a;
    --text-light: #ffffff;
  }
  * { margin: 0; padding: 0; box-sizing: border-box; }
  html, body { width: 1200px; height: 938px; overflow: hidden; }
  body {
    background: var(--backdrop);
    font-family: "Open Sans", Arial, sans-serif;
    position: relative;
  }

  .card {
    position: absolute;
    width: 560px;
    height: 320px;
    border-radius: 24px;
    overflow: hidden;
    box-shadow: 0 10px 28px rgba(90, 50, 70, 0.18);
  }

  /* Front face */
  .card--front {
    left: 80px;
    top: 110px;
    background: var(--card-white);
  }
  .card--front .frame {
    position: absolute;
    inset: 14px;
    border: 1.2px solid var(--plum-line);
    border-radius: 16px;
  }
  .wash {
    position: absolute;
    border-radius: 50%;
    filter: blur(6px);
  }
  .wash--top-right {
    right: -50px; top: -40px;
    width: 260px; height: 200px;
    background: radial-gradient(ellipse at center, rgba(236,170,190,0.75), rgba(240,200,215,0.35) 55%, rgba(255,255,255,0) 72%);
  }
  .wash--bottom-left {
    left: -60px; bottom: -50px;
    width: 280px; height: 210px;
    background: radial-gradient(ellipse at center, rgba(236,170,195,0.75), rgba(240,205,220,0.35) 55%, rgba(255,255,255,0) 72%);
  }
  .brand {
    position: absolute;
    left: 0; right: 0; top: 92px;
    display: flex;
    flex-direction: column;
    align-items: center;
  }
  .brand__mark {
    width: 64px; height: 64px;
    border: 4px solid var(--plum);
    border-radius: 50%;
    margin-bottom: 20px;
  }
  .brand__name {
    font-size: 30px;
    font-weight: 400;
    letter-spacing: 9px;
    color: var(--ink-grey);
    text-transform: uppercase;
    padding-left: 9px;
  }
  .brand__slogan {
    margin-top: 6px;
    display: flex;
    align-items: center;
    gap: 10px;
    font-size: 12px;
    font-weight: 600;
    letter-spacing: 5px;
    color: var(--ink-grey);
    text-transform: uppercase;
  }
  .brand__slogan::before,
  .brand__slogan::after {
    content: "";
    width: 26px;
    height: 1.5px;
    background: var(--ink-grey);
  }

  /* Back face */
  .card--back {
    left: 560px;
    top: 500px;
    background: var(--magenta);
  }
  .card--back .wash--bottom-left {
    left: -40px; bottom: -60px;
    width: 240px; height: 200px;
    background: radial-gradient(ellipse at center, rgba(225,150,205,0.8), rgba(215,130,190,0.3) 55%, rgba(185,96,155,0) 72%);
  }
  .fashion-art {
    position: absolute;
    right: 0; top: 0;
    width: 300px; height: 100%;
    background: linear-gradient(100deg, rgba(185,96,155,0) 0%, rgba(215,140,192,0.55) 35%, rgba(150,200,190,0.45) 62%, rgba(240,180,60,0.7) 85%, rgba(185,96,155,0.2) 100%);
  }
  .contact {
    position: absolute;
    left: 150px;
    top: 110px;
    width: 330px;
    height: 160px;
    background: var(--panel);
    color: var(--text-light);
    display: flex;
    flex-direction: column;
    align-items: center;
    justify-content: center;
    text-align: center;
    gap: 4px;
  }
  .contact__phone { font-size: 14px; letter-spacing: 0.5px; }
  .contact__email { font-size: 20px; letter-spacing: 0.5px; margin-bottom: 4px; }
  .contact__pin { width: 16px; height: 20px; }
  .contact__address { font-size: 14px; line-height: 1.5; }
</style>
</head>
<body>

  <section class="card card--front" aria-label="Business card front">
    <div class="wash wash--top-right" role="img" aria-label="Soft pink watercolour wash"></div>
    <div class="wash wash--bottom-left" role="img" aria-label="Soft pink watercolour wash"></div>
    <div class="frame"></div>
    <div class="brand">
      <div class="brand__mark"></div>
      <div class="brand__name">Gownhaven</div>
      <div class="brand__slogan">Glam for rent</div>
    </div>
  </section>

  <section class="card card--back" aria-label="Business card back">
    <div class="wash wash--bottom-left" role="img" aria-label="Pink watercolour wash"></div>
    <div class="fashion-art" role="img" aria-label="Fashion sketch of women wearing evening outfits"></div>
    <div class="contact">
      <p class="contact__phone">00-0123456789 / 00-0123456789</p>
      <p class="contact__email">info@email.com</p>
      <svg class="contact__pin" viewBox="0 0 16 20" aria-hidden="true">
        <path d="M8 0C3.6 0 0 3.4 0 7.6 0 13 8 20 8 20s8-7 8-12.4C16 3.4 12.4 0 8 0z" fill="#ffffff"/>
        <circle cx="8" cy="7.5" r="3" fill="#8a3a6e"/>
      </svg>
      <p class="contact__address">Lorem Ipsum is simply dummy text<br>of the printing</p>
    </div>
  </section>

</body>
</html>
```